Leading inbound Tour Operator Velvet Pine Travel needs an e-mail newsletter design and html template

Introduction
We need a newsletter design for a experienced tour-company based in Los Angeles called Velvet Pine Travel Inc www.velvetpinetravel.com. We are leading inbound Tour Operator, serving Russian-speaking travelers in North America, and we are in business for over 14 years. We provide travel services to our customers including professional tour guide services on East coast and West Coast, coach bus-tours, private transportation, and much more.

Technical specifications for production design html-template of 2 types e-mail-newsletters in russian language.

Company Name
Velvet Pine Travel Inc http://velvetpinetravel.com

Goal
To increase the involvement of Target Audience in the interaction with the brand, increase loyalty, increase interest in the services of the company, increasing the number of tour and services orders. This is why we use direct mail as one of major marketing instruments. This e-mail html template should be constructed the way allowing us to change pictures and texts. It means that we need reusable templates.

Target Audience:
• 1st design template - business partners. Agencies and tour operators from Russia (Moscow, St. Petersburg, Yekaterinburg) and other Russian-language countries: Ukraine, Belarus, Bulgaria, Latvia. It is the middle-class audience, mostly female, professionals in tourism sphere
• 2nd design template -direct customers. Travelers from former CIS countries: Ukrainian 2/3, Russian 1/3 part. Men and women, middle age (35 years and older), in managerial positions in big companies, have average or above average income, modern and active lifestyle, love to travel and learn new things.

Object of advertising
Multi-day bus tours of the East and West Coast USA.
Examples of tours advertised in the newsletter:
• Canyon Dream Route VIP – http://velvetpinetravel.ru/en/tours/canyon-dream-route-vip/
• Canyon Dream Route – http://velvetpinetravel.ru/en/tours/canyon-dream-route-11-days/
• Whole Continent Loop – http://velvetpinetravel.ru/en/tours/continent-loop/
• Atlantic Shore Journey - http://velvetpinetravel.ru/en/tours/atlantic-shore-journey-11-days/
• City of Palms Circuit - http://velvetpinetravel.ru/en/tours/palms-circuit/
• Desert Lights Trip - http://velvetpinetravel.ru/en/tours/desert-lights-2-days/

Description of the advertised tour
Multi-day bus tours for 50 people. Cost is average. The tour price includes: transfers between cities, excursions along the route, DBL hotel accommodation and breakfasts.

This is important
There is a lot of e-mails everyday sent about tourism, our goal is to stand out of the competitors, and to present company’s service clear and understandable, engaging and interesting at the same time.

Corporate Identity
Color: gold (5/29/100/0), red (14/99/100/0) combined with black / white.
Font: Century Gothic Helvetica OR
Company’s Symbol: Star in the logo (image attached).

Our wishes to the e-mail structure
(Please be advised that the order of the blocks is not required. We would like to get vision of the designer – the best way to present information).
• Block 1 - Contact and logo
• Block 2 – Introductory text ( useful information like news update about USA or any other interesting up-to-date fact catching the eye of the audience) and an important message from the president (including pictures and sign)
• Block 3 - Information about the most important tour in this period of time. This unit should be the most important in the layout, emotionally isolated and eye-catching.
• Block 3 – 6 - scheduled tours or excursions. It is important that the information was easily readable and drawing the attention.

Design difference between 2 types of e-mails
• the 1st design template – for business partners. It should has a table structure, to be very simple and readable even if we will show up to 8 type of tours. So the main descriptions of this template is tabular
• the 2nd design template – for direct customers. It should have the unique and interesting element, which will draw clients’ attention so they wish to read our e-mail from the beginning to the end.

Email size
No larger than 600 px. in width and no more than 2 screens.

Design our previous emails
http://mail7.newsvault-one.com/?u=83a1c7f20b9e4d6605a1f2273&id=c7731ae0d2
http://mail7.newsvault-two.com/?u=83a1c7f20b9e4d6605a1f2273&id=a90d3be517

Attached file:
• Logo
• Tours pictures
• Examples of e-mails that we like PLUS: http://r.plovetrix.com/Q7M/vw.aspx?k=tRAbnqhwXP2kkLmc8fe3WW41qiTxvbnsKaLQ5D-2X8DePzWFkqvCTB$$
http://ridgelandtrust.postrelay9.com/t/ViewEmail/j/4817730AB2298DF1/9C3E5BDA71084F39B2AD61CEEAB3309D

Text for use in e-mail

Contacts
Теl. +1 (800) 555-0148
Skype velvet_pine4182
E-mail info@velvetpinetravel.com

Social networks widgets:
Facebook - https://www.facebook.com/velvetpinetravel.ru
Vkontakte - http://vk.com/velvetpinetravel
Instagram - http://instagram.com/velvetpinetravel
Twitter - https://twitter.com/VelvetPineTrips
Youtube -https://www.youtube.com/channel/UCq7TZ2M9wlkRB_dXaPoLxSe

Introductory text
«Добрый день!

В США прибыла рекордная группа туристов из Китая. Количество путешественников превысело 6 000 человек! Что же привлекает в Америке путешественников со всего мира? Вы можете увидеть и оценить главные достопримечательности Запада Америки на нашем официальном видео-канале на YouTube. Приятного просмотра!

C уважением, Аркадий Лосев
президент компании Velvet Pine Travel Inc.»

Description of main advertise tour
Picture, Name, Dates, Cost, Duration, Itinerary, Link to site «View»

«Каньонные Дали США

Даты заездов 12.09, 03.10, 31.10
Продолжительность 11 дней
Стоимость на чел. $ 1 495

Программа Санта-Барбара - Сан-Франциско - Йосемити - Лас-Вегас - Долина Смерти - каньон Антилопы - трасса 66 - Гранд Каньон - Сан-Диего - Лос-Анджелес
Узнать подробнее»

Scheduled tours or excursions
Name of this block – РАСПИСАНИЕ ТУРОВ VELVET PINE TRAVEL
Description for each tours – Picture, Date, Name, Cost, Duration, Link to site «View»
«08.06
Лос-Анджелес
$ 95 / 6 часов
Подробнее»

Industry/Entity Type

It Company

```html
<!DOCTYPE html>
<html lang="ru">
<head>
<meta charset="utf-8">
<title>Расписание туров Velvet Pine Travel</title>
<link rel="stylesheet" href="https://fonts.googleapis.com/css2?family=Jost:wght@400;500;600;700&family=Arimo:wght@400&display=swap">
<style>
  :root {
    --brand-red: #d6262c;
    --text-dark: #222222;
    --text-body: #333333;
    --rule-grey: #c4c4c4;
    --band-grey: #e7e7e7;
    --page-bg: #ffffff;
    --white: #ffffff;
    --social-sky: #28a9e0;
    --social-navy: #2f4c9a;
    --social-red: #e0201b;
  }
  * { box-sizing: border-box; margin: 0; padding: 0; }
  html, body {
    width: 1057px;
    height: 1200px;
    overflow: hidden;
    background: var(--page-bg);
  }
  .stage {
    width: 900px;
    height: 1022px;
    transform: scale(1.1744);
    transform-origin: 0 0;
    position: relative;
  }
  .newsletter {
    position: absolute;
    left: 150px;
    top: 10px;
    width: 600px;
  }
  .rule {
    height: 3px;
    background: var(--rule-grey);
  }
  .schedule-title {
    height: 48px;
    padding: 15px 0 0 20px;
    font-family: "Jost", "Century Gothic", sans-serif;
    font-weight: 600;
    font-size: 17px;
    letter-spacing: 0.2px;
    color: var(--text-dark);
    text-transform: uppercase;
  }
  .tour-grid {
    display: grid;
    grid-template-columns: 199px 199px 199px;
    column-gap: 1.5px;
  }
  .tour-card { height: 372px; }
  .tour-photo { height: 215px; width: 100%; }
  .tour-info {
    padding: 12px 0 0 17px;
    font-family: "Jost", "Century Gothic", sans-serif;
    font-size: 13.5px;
    line-height: 22px;
  }
  .tour-dates, .tour-city {
    color: var(--brand-red);
    font-weight: 600;
  }
  .tour-price { color: var(--text-body); font-weight: 400; }
  .tour-button {
    display: flex;
    align-items: center;
    justify-content: center;
    margin: 10px 0 0 12px;
    width: 178px;
    height: 40px;
    background: var(--brand-red);
    color: var(--white);
    font-family: "Jost", "Century Gothic", sans-serif;
    font-weight: 600;
    font-size: 14px;
    text-decoration: none;
  }
  .photo-hollywood { background: linear-gradient(160deg, #2f7fd0 0%, #4f94d6 45%, #3d6b3a 80%, #c9d3d8 100%); }
  .photo-sunset { background: linear-gradient(180deg, #f7b24a 0%, #f6c46c 40%, #d98a35 75%, #5a3b1c 100%); }
  .photo-bridge { background: linear-gradient(180deg, #2c7fd2 0%, #7fb5e4 50%, #c2533a 62%, #8d8f94 85%, #6a6d72 100%); }
  .photo-skyline { background: linear-gradient(180deg, #3b8fe0 0%, #a8cdee 40%, #9a9a98 70%, #5c5954 100%); }
  .photo-church { background: linear-gradient(180deg, #1f5fbf 0%, #6f98d0 35%, #d9d7d1 60%, #8e8a84 100%); }
  .photo-resort { background: linear-gradient(180deg, #2c72c8 0%, #a9c4de 35%, #d8c49a 60%, #5e8c5a 78%, #57b3b5 100%); }

  .social-band {
    margin-top: 30px;
    border-top: 3px solid var(--rule-grey);
    border-bottom: 3px solid var(--rule-grey);
    background: var(--band-grey);
    height: 53px;
    display: flex;
    justify-content: center;
    align-items: center;
    gap: 17px;
  }
  .social-dot {
    width: 24px;
    height: 24px;
    border-radius: 50%;
    display: block;
  }
  .social-dot.sky { background: var(--social-sky); margin-left: -16px; }
  .social-dot.navy { background: var(--social-navy); }
  .social-dot.red { background: var(--social-red); }

  .footer {
    padding-top: 15px;
    text-align: center;
    font-family: "Arimo", Arial, sans-serif;
    font-size: 11.5px;
    line-height: 17.5px;
    color: var(--text-body);
  }
  .footer-legal { margin-top: 15px; line-height: 14.5px; }
  .footer-legal .copyright { margin-bottom: 4px; }
  .unsubscribe { color: var(--text-body); text-decoration: underline; }
</style>
</head>
<body>
<div class="stage">
  <main class="newsletter">
    <div class="rule"></div>
    <h1 class="schedule-title">Расписание туров Velvet Pine Travel</h1>

    <section class="tour-grid">
      <article class="tour-card">
        <div class="tour-photo photo-hollywood" role="img" aria-label="Пальма и уличный указатель на бульваре в Голливуде на фоне голубого неба"></div>
        <div class="tour-info">
          <p class="tour-dates">24.06</p>
          <p class="tour-city">Лос-Анджелес</p>
          <p class="tour-price">$ 95 / 6 часов</p>
        </div>
        <a class="tour-button" href="#">Узнать подробнее</a>
      </article>
      <article class="tour-card">
        <div class="tour-photo photo-sunset" role="img" aria-label="Пальмы и небоскрёбы Лос-Анджелеса в золотом закатном свете"></div>
        <div class="tour-info">
          <p class="tour-dates">27.06, 25.07, 08.08</p>
          <p class="tour-city">Лос-Анджелес</p>
          <p class="tour-price">$ 95 / 6 часов</p>
        </div>
        <a class="tour-button" href="#">Узнать подробнее</a>
      </article>
      <article class="tour-card">
        <div class="tour-photo photo-bridge" role="img" aria-label="Красный подвесной мост с автомобилями под голубым небом"></div>
        <div class="tour-info">
          <p class="tour-dates">24.06</p>
          <p class="tour-city">Лос-Анджелес</p>
          <p class="tour-price">$ 95 / 6 часов</p>
        </div>
        <a class="tour-button" href="#">Узнать подробнее</a>
      </article>

      <article class="tour-card">
        <div class="tour-photo photo-skyline" role="img" aria-label="Панорама небоскрёбов Манхэттена под облачным небом"></div>
        <div class="tour-info">
          <p class="tour-dates">24.06</p>
          <p class="tour-city">Лос-Анджелес</p>
          <p class="tour-price">$ 95 / 6 часов</p>
        </div>
        <a class="tour-button" href="#">Узнать подробнее</a>
      </article>
      <article class="tour-card">
        <div class="tour-photo photo-church" role="img" aria-label="Белое здание с куполом и стеклянная башня на фоне синего неба"></div>
        <div class="tour-info">
          <p class="tour-dates">27.06, 25.07, 08.08</p>
          <p class="tour-city">Лос-Анджелес</p>
          <p class="tour-price">$ 95 / 6 часов</p>
        </div>
        <a class="tour-button" href="#">Узнать подробнее</a>
      </article>
      <article class="tour-card">
        <div class="tour-photo photo-resort" role="img" aria-label="Отель-курорт у бирюзового озера под летним небом"></div>
        <div class="tour-info">
          <p class="tour-dates">24.06</p>
          <p class="tour-city">Лос-Анджелес</p>
          <p class="tour-price">$ 95 / 6 часов</p>
        </div>
        <a class="tour-button" href="#">Узнать подробнее</a>
      </article>
    </section>

    <nav class="social-band">
      <a class="social-dot sky" href="#"></a>
      <a class="social-dot navy" href="#"></a>
      <a class="social-dot red" href="#"></a>
    </nav>

    <footer class="footer">
      <p>Velvet Pine Travel, Inc.</p>
      <p>4150 W. Meridian Ave. Suite 310 · West Hollywood · CA 90046</p>
      <p>toll free 1.800.555.0148 · office 323.555.0172 · fax 323.555.0193</p>
      <div class="footer-legal">
        <p class="copyright">Copyright © 2014 Velvet Pine Travel, Inc., All rights reserved.</p>
        <p>Вы получили данный e-mail, потому что находитесь в нашей базе данных. Если вы больше не хотите<br>получать нашу рассылку, пожалуйста, нажмите <a class="unsubscribe" href="#">отписаться от рассылки</a>.</p>
      </div>
    </footer>
  </main>
</div>
</body>
</html>
```